Redesign of page from emergency manual

Please redesign this PDF to look better. Please don't include any stock photos. It must be legible. Making some words bold is probably a good idea.

Here are some things I like :

https://tarrowbooks.com.au/collections/frontpage/products/the-plk-v2-ebook

https://img-cd.vostramediafiles.com/qa-ejkwPLOTYY_SuCKbZNu411Qwgjv8YssPxEdzXN93hDkSRjLXK8WmfgbmrJW4ZZ3yUPK=w1052-h592-rw

```html
<!DOCTYPE html>
<html lang="en">
<head>
<meta charset="utf-8">
<title>Hypertension, Acute</title>
<link rel="stylesheet" href="https://fonts.googleapis.com/css2?family=Roboto:wght@300;400;500;700;900&display=swap">
<style>
:root{
  --lime:#c2e83a;
  --lime-bright:#b9e52c;
  --cyan:#6fe6f8;
  --cyan-head:#00cdec;
  --teal:#00a8c6;
  --ink:#1a1a1a;
  --muted:#9aa04a;
  --grey-strip:#ececec;
  --rule:#222;
  --paper:#ffffff;
}
*{box-sizing:border-box;margin:0;padding:0}
html,body{width:1200px;height:927px;overflow:hidden;background:var(--paper)}
body{font-family:"Roboto",Arial,sans-serif;color:var(--ink)}
.page{position:relative;width:1056px;height:816px;transform:scale(1.13636);transform-origin:0 0;overflow:hidden;background:var(--paper)}
.abs{position:absolute}

/* header */
.title-bar{left:0;top:0;width:990px;height:47px;background:var(--lime)}
.title{left:62px;top:0;font-size:38px;font-weight:700;letter-spacing:3.5px;line-height:46px}
.subtitle{left:572px;top:7px;width:400px;text-align:center;font-size:14px;font-weight:700;letter-spacing:1.6px;line-height:18px}

/* side tab */
.side-tab{left:990px;top:0;width:66px;height:816px;background:var(--lime-bright)}
.page-num{left:990px;top:34px;width:66px;text-align:center;font-size:17px;font-weight:700;letter-spacing:1px}
.side-title{left:1001px;top:72px;width:580px;transform-origin:0 0;transform:rotate(90deg) translateY(-44px);font-size:46px;font-weight:700;letter-spacing:3.4px;line-height:44px;white-space:nowrap}
.revision{left:1018px;top:664px;transform-origin:0 0;transform:rotate(90deg);font-size:13px;font-weight:300;color:var(--muted);white-space:nowrap;letter-spacing:.3px}

.left-strip{left:0;top:47px;width:58px;height:633px;background:var(--grey-strip)}

/* pointer arrows */
.pointer{width:34px;height:12px;background:var(--cyan);clip-path:polygon(0 0,72% 0,100% 50%,72% 100%,0 100%)}

/* intro */
.intro{left:67px;top:63px;width:520px;font-size:16px;letter-spacing:.6px;line-height:22px}
.hl{background:var(--lime);padding:1px 2px}
.bullet-list{list-style:none}
.dot-item{position:absolute;font-size:16px;letter-spacing:.6px;line-height:21px}
.dot-item::before{content:"";position:absolute;left:-20px;top:4px;width:13px;height:13px;border-radius:50%;background:var(--cyan)}
.dash-item{position:absolute;font-size:16px;letter-spacing:.6px}

.caution{left:35px;top:278px;width:955px;font-size:16px;letter-spacing:.6px;line-height:23px}
.caution-tag{display:inline-block;background:var(--cyan);padding:0 14px 0 6px;font-weight:700;letter-spacing:1.4px;clip-path:polygon(0 0,92% 0,100% 50%,92% 100%,0 100%)}

/* range table */
.range{left:600px;top:72px;width:380px;border-collapse:collapse;font-size:15px;letter-spacing:.6px}
.range th,.range td{border:1px solid var(--rule);text-align:center;height:29px}
.range .range-head{background:var(--cyan);font-weight:700;letter-spacing:1.2px;font-size:16px;height:33px}
.range .cols th{font-weight:700;font-size:15px}

/* drug table */
.drugs{left:58px;top:360px;width:932px;border-collapse:collapse;font-size:16px;letter-spacing:.6px}
.drugs th{background:var(--cyan-head);height:42px;font-size:36px;font-weight:700;letter-spacing:4px;border:1px solid var(--rule)}
.drugs td{border-bottom:1px solid var(--rule);vertical-align:top;padding:6px 10px;line-height:21px}
.drugs td.action{width:211px;border-right:1px solid var(--rule)}
.drugs tr:last-child td{border-bottom:1px solid var(--rule)}
.drug-line{display:flex;align-items:flex-start;margin-bottom:8px}
.drug-line:last-child{margin-bottom:0}
.sq{flex:none;width:10px;height:10px;background:var(--cyan);margin:6px 10px 0 0}
.drug-name{background:var(--cyan);padding:0 14px 0 5px;margin-right:2px;clip-path:polygon(0 0,93% 0,100% 50%,93% 100%,0 100%)}
.cont{padding-left:0}

/* differential */
.diff{left:0;top:680px;width:990px;height:136px;background:var(--teal)}
.diff-title{left:61px;top:689px;font-size:18px;letter-spacing:.6px}
.diff-col{position:absolute;top:718px;list-style:none;font-size:16px;letter-spacing:.7px;line-height:21px}
.diff-col li{position:relative;padding-left:0}
.diff-col li::before{content:"";position:absolute;left:-20px;top:3px;width:13px;height:13px;border-radius:50%;background:var(--cyan)}
</style>
</head>
<body>
<div class="page">
  <div class="abs title-bar"></div>
  <h1 class="abs title">Hypertension, Acute</h1>
  <p class="abs subtitle">Sustained high blood pressure refractory to treating reversible causes</p>

  <div class="abs side-tab"></div>
  <div class="abs page-num">12</div>
  <div class="abs side-title">Hypertension, Acute</div>
  <div class="abs revision">Revision Feb 2020</div>

  <div class="abs left-strip"></div>

  <div class="abs pointer" style="left:22px;top:66px"></div>
  <p class="abs intro">In pediatrics, hypertension is almost always treated by addressing likely causes such as <span class="hl">light anesthesia</span> or <span class="hl">measurement error:</span></p>

  <div class="dot-item" style="left:91px;top:147px">Ensure correct BP cuff size:&nbsp; cuff bladder<br>width ~ 40%&nbsp; of limb circumference</div>
  <div class="dot-item" style="left:91px;top:206px">Ensure arterial line transducer is at level of heart</div>
  <div class="dash-item" style="left:115px;top:242px">-&nbsp;&nbsp; Consider placing arterial line if not already present</div>

  <table class="abs range">
    <tr><th class="range-head" colspan="3">Hypertensive Blood Pressure Range*</th></tr>
    <tr class="cols"><th>Age (yr)</th><th>Systolic</th><th>Diastolic</th></tr>
    <tr><td>newborn</td><td>&gt; 97</td><td>&gt; 70</td></tr>
    <tr><td>1-3</td><td>&gt; 105</td><td>&gt; 61</td></tr>
    <tr><td>4-12</td><td>&gt; 113</td><td>&gt; 86</td></tr>
  </table>

  <p class="abs caution"><span class="caution-tag">* CAUTION:</span> Anti-hypertensive drugs are almost never needed for routine pediatric cases. These medications are used almost exclusively for specialized cardiac, neurosurgical, or endocrine (pheochromocytoma) cases. Consult an expert before use. Rule-out increased ICP.</p>

  <table class="abs drugs">
    <tr><th>Action</th><th>Drug (IV Dosing)</th></tr>
    <tr style="height:70px">
      <td class="action">Direct smooth muscle relaxation</td>
      <td>
        <div class="drug-line"><span class="sq"></span><span><span class="drug-name">Sodium nitroprusside</span> 0.5-10 MICROgrams/kg/min</span></div>
        <div class="drug-line"><span class="sq"></span><span><span class="drug-name">HydrALAZINE</span> 0.1-0.2 mg/kg (adult dose 5-10 mg)</span></div>
      </td>
    </tr>
    <tr style="height:98px">
      <td class="action">β-Adrenergic blockade</td>
      <td>
        <div class="drug-line"><span class="sq"></span><span><span class="drug-name">Esmolol</span> 100-500 MICROgrams/kg over 5 min, then<br>25-300 MICROgrams/kg/min</span></div>
        <div class="drug-line"><span class="sq"></span><span><span class="drug-name">Labetalol (also α effect)</span> 0.2-1 mg/kg q 10 min;&nbsp;&nbsp; 0.4-3 mg/kg/<i>hour</i> (infusion)</span></div>
      </td>
    </tr>
    <tr style="height:67px">
      <td class="action">Calcium channel blockade</td>
      <td>
        <div class="drug-line"><span class="sq"></span><span><span class="drug-name">niCARdapine</span> 0.5-5 MICROgrams/kg/min</span></div>
        <div class="drug-line"><span class="sq"></span><span><span class="drug-name">Clevidipine</span> 0.5-3.5 MICROgrams/kg/min</span></div>
      </td>
    </tr>
    <tr style="height:41px">
      <td class="action">D1-dopamine agonist</td>
      <td>
        <div class="drug-line"><span class="sq"></span><span><span class="drug-name">Fenoldopam</span> 0.2-0.8 MICROgrams/kg/min</span></div>
      </td>
    </tr>
  </table>

  <div class="abs diff"></div>
  <div class="abs pointer" style="left:22px;top:695px"></div>
  <h2 class="abs diff-title" style="font-weight:400">Consider Differential (Partial):</h2>
  <ul class="diff-col" style="left:88px">
    <li>Light anesthesia (consider<br>vaporizer or infusion pump<br>empty or malfunctioning)</li>
    <li>Hypercarbia</li>
  </ul>
  <ul class="diff-col" style="left:380px">
    <li>Hypoxemia</li>
    <li>Arterial line transducer too<br>low or BP cuff too small</li>
    <li>Withdrawal (EtOH or opioid)</li>
  </ul>
  <ul class="diff-col" style="left:677px">
    <li>Thyroid Storm</li>
    <li>Pheochromocytoma</li>
    <li>Drug Error</li>
  </ul>
</div>
</body>
</html>
```